Quillex Landing Page & Logo

We are building a landing page for a new blockchain-based project called Quillex. The site should look modern and minimalistic with a very brief description of the upcoming project ("Unlock your Brevitan governance stack. Win weekly prizes and a quarterly jackpot!"), a viper logo (the animal - but can just be lettering) , and a button to subscribe for updates and early access.
Examples of similar pages:
https://pondru.finance/
https://www.zentrimo.org/
https://lumbrecks.com/
https://q8.io/
https://www.tovern.finance/
Crypto Users (Specifically Brevitan holders)

```html
<!DOCTYPE html>
<html lang="en">
<head>
<meta charset="utf-8">
<title>Quillex — Logo &amp; Landing Page</title>
<link rel="stylesheet" href="https://fonts.googleapis.com/css2?family=Montserrat:wght@400&family=Source+Sans+3:wght@400;700&display=swap">
<style>
  :root {
    --board-bg: #ffffff;
    --ink-dark: #0f1d18;
    --brand-green: #1f8a4c;
    --hero-bg: #101c18;
    --hero-text: #c9e4c4;
    --deco-green: #2f6a36;
    --lower-bg: #eeeff1;
    --card-top: #d1e8c8;
    --card-bottom: #b3d9ca;
    --card-title: #1a5a3e;
    --card-text: #555a57;
    --input-bg: #f4f2f3;
    --input-placeholder: #9a9a9a;
    --button-top: #7dc142;
    --button-bottom: #0d7446;
    --white: #ffffff;
  }
  * { box-sizing: border-box; margin: 0; padding: 0; }
  html, body {
    width: 1200px; height: 1000px; overflow: hidden;
    background: var(--board-bg);
  }
  body { position: relative; font-family: "Source Sans 3", sans-serif; }

  /* Primary logo */
  .brand-lockup {
    position: absolute; left: 0; right: 0; top: 92px;
    display: flex; align-items: center; justify-content: center; gap: 26px;
  }
  .brand-mark {
    width: 70px; height: 70px; border-radius: 50%;
    background: var(--brand-green);
  }
  .brand-name {
    font-family: "Montserrat", sans-serif; font-weight: 400;
    font-size: 72px; letter-spacing: 3px; color: var(--ink-dark);
    line-height: 1;
  }

  /* Landing page */
  .landing-page {
    position: absolute; left: 208px; top: 264px;
    width: 783px; height: 602px;
    background: var(--lower-bg);
    box-shadow: 0 12px 40px rgba(0,0,0,0.22);
  }
  .hero {
    position: absolute; left: 0; top: 0; width: 100%; height: 441px;
    background: var(--hero-bg); overflow: hidden;
  }
  .hero-decoration {
    position: absolute; left: 90px; top: 0; width: 620px; height: 380px;
    background: linear-gradient(145deg, transparent 20%, rgba(47,106,54,0.35) 55%, rgba(22,82,52,0.5) 80%, transparent 100%);
    clip-path: polygon(88% 0, 100% 8%, 100% 35%, 40% 100%, 0 100%, 0 85%, 60% 20%, 75% 0);
  }
  .site-header {
    position: absolute; left: 97px; top: 30px;
    display: flex; align-items: center; gap: 10px;
  }
  .site-mark { width: 28px; height: 28px; border-radius: 50%; background: var(--brand-green); }
  .site-name {
    font-family: "Montserrat", sans-serif; font-weight: 400;
    font-size: 21px; letter-spacing: 1.5px; color: var(--white);
  }
  .hero-title {
    position: absolute; left: 0; right: 0; top: 150px;
    text-align: center; font-weight: 400; font-size: 46px;
    line-height: 56px; color: var(--hero-text); letter-spacing: 0.5px;
  }

  .subscribe-card {
    position: absolute; left: 97px; top: 355px; width: 590px; height: 172px;
    border-radius: 26px;
    background: linear-gradient(180deg, var(--card-top), var(--card-bottom));
    box-shadow: 0 4px 10px rgba(0,0,0,0.12);
    text-align: center;
  }
  .subscribe-title {
    position: absolute; left: 0; right: 0; top: 30px;
    font-weight: 700; font-size: 20px; letter-spacing: 0.6px; color: var(--card-title);
  }
  .subscribe-text {
    position: absolute; left: 0; right: 0; top: 60px;
    font-size: 14.5px; color: var(--card-text);
  }
  .email-field {
    position: absolute; left: 103px; top: 97px; width: 244px; height: 37px;
    border-radius: 19px; background: var(--input-bg);
    display: flex; align-items: center; padding-left: 20px; gap: 11px;
    font-size: 14.5px; color: var(--input-placeholder);
  }
  .email-icon { width: 19px; height: 13px; }
  .submit-button {
    position: absolute; left: 370px; top: 97px; width: 116px; height: 37px;
    border-radius: 19px;
    background: linear-gradient(180deg, var(--button-top), var(--button-bottom));
    box-shadow: 0 2px 4px rgba(0,0,0,0.2);
    color: var(--white); font-size: 14.5px;
    display: flex; align-items: center; justify-content: center;
  }
</style>
</head>
<body>
  <header class="brand-lockup">
    <span class="brand-mark"></span>
    <span class="brand-name">Quillex</span>
  </header>

  <main class="landing-page">
    <section class="hero">
      <div class="hero-decoration" role="img" aria-label="Decorative sweep of green snake-scale arcs curving across the hero"></div>
      <div class="site-header">
        <span class="site-mark"></span>
        <span class="site-name">Quillex</span>
      </div>
      <h1 class="hero-title">blockchain-based<br>project</h1>
    </section>

    <section class="subscribe-card">
      <h2 class="subscribe-title">SUBSCRIBE</h2>
      <p class="subscribe-text">subscribe for updates and early access</p>
      <div class="email-field">
        <svg class="email-icon" viewBox="0 0 19 13" aria-hidden="true">
          <rect x="0" y="0" width="19" height="13" fill="#a6a6a6"/>
          <path d="M0 0 L9.5 7 L19 0 M0 13 L7 6 M19 13 L12 6" stroke="#f4f2f3" stroke-width="1.2" fill="none"/>
        </svg>
        <span>Email</span>
      </div>
      <div class="submit-button">Submit</div>
    </section>
  </main>
</body>
</html>
```